Business Card Design

We sell fish products to corporate food companies who then turn these products into final food products for consumers

Industry/Entity Type

Business

Contact Information for Business Card

I need a corporate business card template for a fish products business. We would like it be professional for use in dealing with multi national companies. This company business card template will be used by multiple employees so the following fields must be open to edit (Name, Phone Number and Email address)

```html
<!DOCTYPE html>
<html lang="en">
<head>
<meta charset="UTF-8">
<title>Tidewell Seafoods – Business Card</title>
<link href="https://fonts.googleapis.com/css2?family=Oswald:wght@600&family=Open+Sans:wght@400;600&display=swap" rel="stylesheet">
<style>
  :root {
    --page-bg: #e6e6e4;
    --card-white: #ffffff;
    --card-grey-light: #f4f4f4;
    --card-grey-dark: #d2d2d2;
    --brand-blue: #1f5fae;
    --brand-navy: #144f93;
    --wave-blue: #2a72b8;
    --wave-teal: #3fb8cf;
    --icon-green: #49b36e;
    --text-blue: #2a5fa8;
  }
  * { box-sizing: border-box; margin: 0; padding: 0; }
  html, body { width: 1200px; height: 871px; overflow: hidden; }
  body {
    position: relative;
    background: var(--page-bg);
    font-family: "Open Sans", sans-serif;
  }
  .card {
    position: absolute;
    width: 620px;
    height: 354px;
    border-radius: 3px;
    overflow: hidden;
    box-shadow: 0 10px 24px rgba(0,0,0,0.22);
  }
  .card-back {
    left: 60px; top: 50px;
    background: linear-gradient(135deg, var(--card-grey-light) 0%, var(--card-white) 35%, var(--card-grey-dark) 100%);
    display: flex; align-items: center; justify-content: center;
  }
  .card-front {
    left: 520px; top: 470px;
    background: var(--card-white);
  }
  .brand {
    display: flex; align-items: center; gap: 12px;
    color: var(--brand-blue);
    font-family: "Open Sans", sans-serif;
    font-weight: 600;
    letter-spacing: 0.02em;
    white-space: nowrap;
  }
  .brand-dot {
    border-radius: 50%;
    background: var(--brand-blue);
    flex: none;
  }
  .card-back .brand { font-size: 34px; }
  .card-back .brand-dot { width: 30px; height: 30px; }
  .card-front .brand {
    position: absolute; right: 34px; top: 145px;
    font-size: 26px;
  }
  .card-front .brand-dot { width: 22px; height: 22px; }
  .holder-name {
    position: absolute; left: 36px; top: 38px;
    font-family: "Oswald", sans-serif;
    font-weight: 600;
    font-size: 30px;
    letter-spacing: 0.06em;
    color: var(--text-blue);
    text-transform: uppercase;
  }
  .contact-list {
    position: absolute; left: 36px; top: 100px;
    list-style: none;
    font-size: 14px;
    color: var(--text-blue);
    line-height: 22px;
  }
  .contact-list li { display: flex; align-items: center; gap: 10px; }
  .contact-list svg { width: 13px; height: 13px; flex: none; }
  .wave { position: absolute; left: 0; bottom: 0; width: 620px; height: 354px; }
</style>
</head>
<body>
  <div class="card card-back">
    <div class="brand"><span class="brand-dot"></span>TIDEWELL SEAFOODS</div>
  </div>

  <div class="card card-front">
    <svg class="wave" viewBox="0 0 620 354" aria-hidden="true">
      <path d="M0,180 C140,168 280,215 400,268 C480,302 560,318 620,312 L620,354 L0,354 Z" fill="var(--wave-blue)"/>
      <path d="M0,172 C140,160 280,205 400,258 C480,292 560,308 620,302 L620,314 C560,320 480,304 400,270 C280,217 140,170 0,182 Z" fill="var(--wave-teal)"/>
      <path d="M0,168 C140,156 280,200 400,252 C480,286 560,302 620,296" fill="none" stroke="var(--card-white)" stroke-width="2"/>
    </svg>

    <div class="holder-name">Mara Ellison</div>
    <ul class="contact-list">
      <li>
        <svg viewBox="0 0 16 16"><path d="M3 2h3l1.5 3.5-2 1.2a8 8 0 0 0 3.8 3.8l1.2-2L14 10v3a1 1 0 0 1-1 1A11 11 0 0 1 2 3a1 1 0 0 1 1-1z" fill="none" stroke="var(--icon-green)" stroke-width="1.4"/></svg>
        555 014 3276
      </li>
      <li>
        <svg viewBox="0 0 16 16"><rect x="4" y="1.5" width="8" height="13" rx="1.5" fill="none" stroke="var(--icon-green)" stroke-width="1.4"/><circle cx="8" cy="12" r="0.9" fill="var(--icon-green)"/></svg>
        555 014 3276
      </li>
      <li>
        <svg viewBox="0 0 16 16"><rect x="1.5" y="3.5" width="13" height="9" fill="none" stroke="var(--icon-green)" stroke-width="1.4"/><path d="M1.5 3.5 8 9l6.5-5.5" fill="none" stroke="var(--icon-green)" stroke-width="1.4"/></svg>
        mara@tidewellseafoods.com
      </li>
    </ul>

    <div class="brand"><span class="brand-dot"></span>TIDEWELL SEAFOODS</div>
  </div>
</body>
</html>
```